Driving-coach/trainer who wants to inform about the offer and how I can help people to drive more re

I need a flyer that informs potential customers about my offer.

DL size 210 mm x 99 mm, vertical!

I'm a trainer/coach who helps people to drive a car more relaxed, without fear and more confident.

It's a one to one training. I do train people in their own car. It gets people their freedom back to go where and when they like to go by own car...

Target Market(s)

People (man an woman) who are afraid of driving a car, or are very stressed while driving....

Industry/Entity Type

Life Coaching

Font styles to use
Sans Serif

Colors
acd136

Requirements
Must have
• Page 1:
• -my offer (see text-pdf)
• -three fotos (see attached files "Pixmarra") of people who are satisfied with my offer
• Page 2:
• -advantages in the work with me.
• -contact information
• -and a picture of me (see attached file) next to the contact information or the advantages of my work
• -my logo (see attached file) on Page 1 + 2
• -i like a "clear" and structured layout. "Less is more"

```html
<!DOCTYPE html>
<html lang="de">
<head>
<meta charset="utf-8">
<title>Fahrangst erfolgreich loswerden – Flyer</title>
<link rel="stylesheet" href="https://fonts.googleapis.com/css2?family=Ubuntu:wght@500;700&family=Open+Sans:wght@300;400;700&family=Oswald:wght@500&display=swap">
<style>
  :root {
    --backdrop: #1c1c1d;
    --paper: #ffffff;
    --green-head: #4ea83b;
    --green-text: #5aab3c;
    --green-band: #1f7e36;
    --green-light: #8dc63f;
    --green-pill: #6cbd3d;
    --grey-text: #4f4f4f;
  }
  * { margin: 0; padding: 0; box-sizing: border-box; }
  html, body { width: 1200px; height: 2215px; overflow: hidden; background: var(--backdrop); }
  .flyer {
    position: absolute; left: 144px; top: 138px;
    width: 912px; height: 1938px;
    background: var(--paper); overflow: hidden;
    font-family: "Open Sans", sans-serif;
  }
  .hero-photo {
    position: absolute; left: 0; top: 0; width: 912px; height: 760px;
    background:
      linear-gradient(to bottom, rgba(255,255,255,0) 60%, #fff 100%),
      linear-gradient(100deg, #c9c5a8 0%, #a9a98a 30%, #dcd9d2 48%, #e9d7c2 65%, #f0e3d6 100%);
  }
  .headline {
    position: absolute; left: 55px; top: 62px;
    font-family: "Ubuntu", sans-serif; font-weight: 700;
    font-size: 62px; line-height: 68px; letter-spacing: 1px;
    color: var(--green-head); text-transform: uppercase;
  }
  .questions {
    position: absolute; left: 0; top: 700px; width: 912px;
    text-align: center; font-size: 43px; line-height: 50px; color: var(--grey-text);
  }
  .questions p + p { margin-top: 24px; }
  .questions .accent { color: var(--green-text); }
  .band {
    position: absolute; left: 0; top: 1021px; width: 912px; height: 687px;
    background: var(--green-band);
  }
  .pill-main {
    position: absolute; left: 74px; top: 965px; width: 780px; height: 124px;
    background: #fff; border: 5px solid var(--green-text); border-radius: 62px;
    box-shadow: 0 12px 14px rgba(0,0,0,.35);
    display: flex; align-items: center; justify-content: center;
    font-family: "Oswald", sans-serif; font-weight: 500; font-size: 60px;
    color: var(--green-text); text-transform: uppercase;
  }
  .intro {
    position: absolute; left: 0; top: 1127px; width: 912px; text-align: center;
    font-weight: 700; font-size: 30px; color: var(--green-light);
  }
  .col { position: absolute; top: 1186px; color: #fff; font-size: 25.5px; line-height: 32px; }
  .col-left { left: 92px; width: 360px; }
  .col-right { left: 506px; width: 370px; }
  .col p + p { margin-top: 22px; }
  .col b { font-weight: 700; }
  .check-item { position: relative; }
  .check-icon { position: absolute; left: -42px; top: 2px; width: 32px; height: 32px; }
  .pill-cta {
    position: absolute; left: 109px; top: 1664px; width: 707px; height: 84px;
    background: linear-gradient(#7fcb47, var(--green-pill));
    border: 4px solid #fff; border-radius: 42px;
    box-shadow: 0 12px 14px rgba(0,0,0,.3);
    display: flex; align-items: center; justify-content: center;
    font-weight: 700; font-size: 37px; color: #fff;
  }
  .coach-name {
    position: absolute; left: 74px; top: 1782px;
    font-family: "Ubuntu", sans-serif; font-weight: 500;
    font-size: 47px; letter-spacing: 4px; color: var(--green-text);
  }
  .coach-role {
    position: absolute; left: 74px; top: 1842px;
    font-family: "Ubuntu", sans-serif; font-weight: 500;
    font-size: 37px; letter-spacing: 3px; color: var(--green-text);
  }
</style>
</head>
<body>
<main class="flyer">
  <div class="hero-photo" role="img" aria-label="Fotografie: lächelnde junge Frau lehnt aus dem Autofenster und zeigt den Daumen nach oben"></div>
  <h1 class="headline">Fahrangst<br>erfolgreich<br>loswerden!</h1>

  <div class="questions">
    <p><span class="accent">Sie wollen</span> endlich entspannt<br>und sicher Auto fahren?</p>
    <p>Panikattacken beim<br><span class="accent">Autofahren</span> überwinden?</p>
  </div>

  <div class="band"></div>
  <div class="pill-main">Dann sind Sie hier richtig!</div>

  <p class="intro">Kommt Ihnen eine dieser Situationen bekannt vor?</p>

  <div class="col col-left">
    <p class="check-item">
      <svg class="check-icon" viewBox="0 0 32 32" aria-hidden="true"><circle cx="16" cy="16" r="13" fill="none" stroke="#fff" stroke-width="3"/><path d="M9 16l5 5 10-11" fill="none" stroke="#8dc63f" stroke-width="4" stroke-linecap="round" stroke-linejoin="round"/></svg>
      <b>Angst oder Panikattacken</b> begleiten Sie beim Autofahren. Vielleicht <b>vermeiden</b> Sie deshalb das Autofahren komplett. - Sie möchten <b>angstfrei und/ oder ohne Panikattacken</b> fahren.
    </p>
    <p class="check-item">
      <svg class="check-icon" viewBox="0 0 32 32" aria-hidden="true"><circle cx="16" cy="16" r="13" fill="none" stroke="#fff" stroke-width="3"/><path d="M9 16l5 5 10-11" fill="none" stroke="#8dc63f" stroke-width="4" stroke-linecap="round" stroke-linejoin="round"/></svg>
      Sie <b>trauen sich das Autofahren nicht (mehr) zu.</b> - Sie wünschen sich, <b>sicher, entspannt und stressfrei Auto zu fahren.</b>
    </p>
  </div>

  <div class="col col-right">
    <p><b>Autofahren</b> erleben Sie unter h<b>oher Anspannung und Stress.</b> - Sie wünschen sich, Autofahren <b>sicher und entspannt</b> zu erleben.</p>
    <p>Bestimmte Situationen (z.B. <b>Autobahn, Baustellen, Stadtvekehr</b>...) bereiten Ihnen <b>großen Stress.</b> - Sie möchten diese Situationen <b>souveräner</b> meistern.</p>
  </div>

  <div class="pill-cta">Das muss nicht so bleiben!</div>

  <p class="coach-name">Sabine Morlandt</p>
  <p class="coach-role">Fahrangst–Bewältigungs–Coach</p>
</main>
</body>
</html>
```